New Packaging Design for Olives

We are looking for a new packaging design for our product.
- Clear plastic cup container
- 90mm round lid and tapers down to 45mm base
- We do not want a box
- We would like a cardboard wrap around.
Product:
- Pitted Kalamata Olives
- 90g Net
We would like to product to be displayed from top view and side view.
We would like an image of kalamata olives on the packaging
our logo to appear on top and side
the bottom of the packaging to have room for a bar code, ingredients & nutritional panel.
This product is designed to target the accommodation/hotel market and we are wanting a classy looking design to attract mini bar customers.
Attached is an image of the cup & an internal mock up and our company logo.
We need a design that will seamlessly work across a variety of products including salsa, chilli sauce, tomato sauce and others.
Hotel Mini bar at 4 to 5 star hotels
Hotel

```html
<!DOCTYPE html>
<html lang="en">
<head>
<meta charset="utf-8">
<title>Kalamata Olives – Wrap Label</title>
<link href="https://fonts.googleapis.com/css2?family=Tinos:wght@400;700&display=swap" rel="stylesheet">
<style>
  :root {
    --page: #ffffff;
    --label-black: #0b0b0b;
    --label-charcoal: #3a3a3a;
    --gold-light: #e9dca0;
    --gold-mid: #c9b25d;
    --gold-dark: #8c7632;
    --kalamata-red: #c8202b;
    --olive-grey-dark: #1e1e1e;
    --olive-grey-light: #8a8a8a;
    --pitted-green: #7d9a3a;
    --net-white: #f4f1e6;
    --serif: "Tinos", "Times New Roman", serif;
  }
  * { margin: 0; padding: 0; box-sizing: border-box; }
  html, body { width: 1200px; height: 821px; overflow: hidden; background: var(--page); }
  .canvas { position: relative; width: 1200px; height: 821px; font-family: var(--serif); }

  .lid-label { position: absolute; left: 80px; top: 70px; width: 505px; height: 457px; overflow: hidden; }
  .lid-label svg { position: absolute; inset: 0; }

  .label-text { position: absolute; line-height: 1; white-space: nowrap; }
  .lid-label .kalamata { right: 37px; top: 12px; font-size: 48px; color: var(--kalamata-red); }
  .lid-label .olives {
    right: 32px; top: 40px; font-size: 104px;
    background: linear-gradient(180deg, var(--olive-grey-dark) 20%, var(--olive-grey-light) 100%);
    -webkit-background-clip: text; background-clip: text; color: transparent;
  }
  .lid-label .pitted { right: 39px; top: 137px; font-size: 37px; font-weight: 700; color: var(--pitted-green); }
  .lid-label .net { right: 20px; top: 419px; font-size: 26px; font-weight: 700; color: var(--net-white); }

  .brand-name { position: absolute; font-family: var(--serif); font-weight: 400; color: var(--gold-mid); line-height: 1; white-space: nowrap; }
  .lid-label .brand-name { left: 18px; top: 400px; font-size: 44px; }

  .side-band {
    position: absolute; left: 82px; top: 577px; width: 503px; height: 177px;
    background: linear-gradient(180deg, #000 0%, #0d0d0d 60%, #1c1c1c 100%);
  }
  .side-band .kalamata { left: 16px; top: 71px; font-size: 36px; color: var(--kalamata-red); }
  .side-band .olives {
    left: 14px; top: 96px; font-size: 78px;
    background: linear-gradient(180deg, #2a2a2a 0%, #7a7a7a 100%);
    -webkit-background-clip: text; background-clip: text; color: transparent;
  }
  .side-band .brand-name { right: 22px; top: 128px; font-size: 32px; }
</style>
</head>
<body>
<main class="canvas">

  <section class="lid-label">
    <svg width="505" height="457" viewBox="0 0 505 457">
      <defs>
        <linearGradient id="lidBackground" x1="0" y1="0" x2="1" y2="1">
          <stop offset="0" stop-color="var(--label-charcoal)"/>
          <stop offset="0.45" stop-color="var(--label-black)"/>
          <stop offset="1" stop-color="#262626"/>
        </linearGradient>
        <linearGradient id="goldSweep" x1="0" y1="0" x2="1" y2="1">
          <stop offset="0" stop-color="var(--gold-dark)"/>
          <stop offset="0.35" stop-color="var(--gold-light)"/>
          <stop offset="0.7" stop-color="var(--gold-mid)"/>
          <stop offset="1" stop-color="var(--gold-dark)"/>
        </linearGradient>
        <radialGradient id="oliveTones" cx="0.45" cy="0.5" r="0.55">
          <stop offset="0" stop-color="#4e2428"/>
          <stop offset="0.6" stop-color="#6e3b38"/>
          <stop offset="0.85" stop-color="#d6cf94" stop-opacity="0.5"/>
          <stop offset="1" stop-color="#ffffff" stop-opacity="0"/>
        </radialGradient>
        <clipPath id="whiteField">
          <ellipse cx="384" cy="104" rx="330" ry="244"/>
        </clipPath>
      </defs>
      <rect width="505" height="457" fill="url(#lidBackground)"/>
      <ellipse cx="370" cy="112" rx="352" ry="262" fill="url(#goldSweep)"/>
      <ellipse cx="384" cy="104" rx="330" ry="244" fill="#ffffff"/>
      <g clip-path="url(#whiteField)">
        <ellipse cx="300" cy="265" rx="160" ry="100" fill="url(#oliveTones)"
                 role="img" aria-label="Photo of glossy pitted kalamata olives in olive oil with a rosemary sprig"/>
      </g>
    </svg>

    <div class="label-text kalamata">KALAMATA</div>
    <div class="label-text olives">OLIVES</div>
    <div class="label-text pitted">PITTED</div>

    <span class="brand-name">Harwick</span>
    <div class="label-text net">90G NET</div>
  </section>

  <section class="side-band">
    <div class="label-text kalamata">KALAMATA</div>
    <div class="label-text olives">OLIVES</div>
    <span class="brand-name">Harwick</span>
  </section>

</main>
</body>
</html>
```